BBQ Catering & Pop-up Restaurant

I'm a catering company and a pop-up restaurant and need a website that will have the following at minimum (I'm open to suggestions): about me section, menu section, events section, a pre-order page. Here is an example of a site that I really like ... https://hollowpitsmoke.example/ . I want to have a pre-order page where people can place orders online and the ability to take credit card payments. I've included a word doc with a draft write up to get started.
Updates

Project Deadline Extended
Reason: I am awaiting feedback from my partner and will be in touch ASAP.

Target Market(s)

BBQ Lovers

Industry/Entity Type

Caterer

Font styles to use
Serif
Other font styles liked:
• we can use multiple fonts where appropriate. I also like a faded, woody type font - which reminds me of the old western movies

Colors

Designer to choose colors to be used in the design.

Requirements
Must have
• I want
• - a smokey, woody, bbq type feel to the site.
• - my logo to be utilized
• - colors I like should compliment the colors in my logo
• - link to sign up for a news letter/ mailing list and something on the back end to capture data
Nice to have
• NA
Should not have
• NA

```html
<!DOCTYPE html>
<html lang="en">
<head>
<meta charset="utf-8">
<title>Emberly Smokehouse</title>
<link href="https://fonts.googleapis.com/css2?family=Oswald:wght@300;400;500;600&family=Open+Sans:wght@400;600&family=Dancing+Script:wght@400;600&family=Lora:ital@1&family=Jost:wght@400;500&display=swap" rel="stylesheet">
<style>
:root{
  --gold:#c8963e;
  --gold-soft:#d4a24c;
  --ink:#15151a;
  --panel:#1d1d22;
  --menu-bg:#17171c;
  --white:#ffffff;
  --muted:#8a8a90;
  --footer:#141416;
  --footer-bar:#0c0c0e;
  --blog-text:#333;
}
*{box-sizing:border-box;margin:0;padding:0}
html,body{width:1200px;height:3152px;overflow:hidden}
body{position:relative;background:var(--ink);font-family:"Open Sans",sans-serif;color:var(--white)}
.abs{position:absolute}
.section{position:absolute;left:0;width:1200px;overflow:hidden}

/* hero */
.hero{top:0;height:634px}
.hero-photo{position:absolute;inset:0;background:
  radial-gradient(circle at 12% 22%,rgba(190,150,70,.55) 0,rgba(190,150,70,0) 170px),
  radial-gradient(circle at 70% 12%,rgba(220,200,160,.45) 0,rgba(220,200,160,0) 150px),
  radial-gradient(circle at 50% 40%,rgba(200,90,40,.4) 0,rgba(200,90,40,0) 170px),
  radial-gradient(circle at 90% 40%,rgba(170,60,30,.6) 0,rgba(170,60,30,0) 230px),
  radial-gradient(ellipse at 20% 90%,rgba(230,220,210,.35) 0,rgba(230,220,210,0) 260px),
  linear-gradient(160deg,#5a3a22 0%,#46301e 45%,#2c1c10 100%)}
.hero-shade{position:absolute;inset:0;background:rgba(0,0,0,.28)}
.brand{position:absolute;left:110px;top:76px;font-family:"Oswald",sans-serif;font-weight:600;font-size:38px;letter-spacing:4px;color:var(--white)}
.nav a{position:absolute;top:68px;font-family:"Oswald",sans-serif;font-weight:500;font-size:10px;letter-spacing:.5px;color:var(--white);text-decoration:none;text-transform:uppercase;white-space:nowrap}
.hero-title{position:absolute;top:262px;width:100%;text-align:center;font-family:"Oswald",sans-serif;font-weight:300;font-size:50px;letter-spacing:12px}
.hero-sub{position:absolute;top:348px;width:100%;text-align:center;font-size:16px}
.btn{position:absolute;display:flex;align-items:center;justify-content:center;border-radius:20px;font-family:"Oswald",sans-serif;font-weight:600;font-size:11px;letter-spacing:1px;text-transform:uppercase;white-space:nowrap}
.btn-outline{border:2px solid var(--white);background:#1a1512}
.btn-gold{background:var(--gold)}

/* book + welcome */
.book{top:634px;height:521px}
.wood{position:absolute;inset:0;background:
  radial-gradient(ellipse at 80% 60%,rgba(120,70,40,.6) 0,rgba(120,70,40,0) 420px),
  linear-gradient(90deg,#2e1c12 0%,#4a2e1e 30%,#3c2416 55%,#5a3624 80%,#3a2216 100%)}
.wood-shade{position:absolute;inset:0;background:linear-gradient(90deg,rgba(0,0,0,.3),rgba(0,0,0,.05))}
.book-panel{position:absolute;left:120px;top:0;width:468px;height:521px;background:var(--panel)}
.sec-title{font-family:"Oswald",sans-serif;font-weight:400;font-size:21px;letter-spacing:5px;text-transform:uppercase}
.script{font-family:"Dancing Script",cursive;color:var(--gold);font-size:19px}
.rule{height:2px;width:48px;background:var(--gold)}
.field{position:absolute;background:#26262b;font-size:12px;color:#9a9aa0;padding:8px 10px}
.welcome-text{position:absolute;left:697px;top:832px;width:388px;font-size:12px;line-height:20.5px;color:#eee}

/* special */
.special{top:1155px;height:531px}
.special-bg{position:absolute;inset:0;background:
  radial-gradient(ellipse at 30% 55%,rgba(170,120,50,.7) 0,rgba(170,120,50,0) 360px),
  radial-gradient(circle at 72% 12%,rgba(120,120,110,.45) 0,rgba(120,120,110,0) 140px),
  linear-gradient(180deg,#1e1812,#121110)}
.dish{position:absolute;top:1338px;width:220px}
.dish-photo{width:220px;height:222px;border:2px solid #8a5a2a}
.dish-name{text-align:center;font-family:"Oswald",sans-serif;font-weight:500;font-size:14px;margin-top:10px}
.dish-rule{height:1px;background:var(--gold);margin-top:8px}
.dish-price{text-align:center;font-family:"Oswald",sans-serif;font-weight:600;font-size:17px;margin-top:10px}

/* menu */
.menu{top:1686px;height:618px;background:var(--menu-bg)}
.tab{position:absolute;top:175px;height:30px;width:92px;border:1px solid #55555c;display:flex;align-items:center;justify-content:center;font-family:"Oswald",sans-serif;font-weight:600;font-size:11px;letter-spacing:1px}
.tab.active{border:2px solid var(--gold);color:var(--gold)}
.item{position:absolute;width:395px}
.item-thumb{position:absolute;left:0;top:0;width:50px;height:50px;border-radius:50%}
.item-name{position:absolute;left:67px;top:0;font-family:"Oswald",sans-serif;font-weight:500;font-size:14px}
.item-price{position:absolute;right:0;top:0;font-family:"Oswald",sans-serif;font-weight:500;font-size:14px;color:var(--gold)}
.item-desc{position:absolute;left:67px;top:22px;width:330px;font-family:"Lora",serif;font-style:italic;font-size:11px;line-height:19px;color:var(--muted)}

/* blog */
.blog{top:2304px;height:571px;background:#fff}
.blog-bg{position:absolute;left:0;top:112px;width:1200px;height:459px;background:
  radial-gradient(ellipse at 12% 40%,rgba(255,230,160,.9) 0,rgba(255,230,160,0) 320px),
  radial-gradient(ellipse at 92% 70%,rgba(150,120,90,.7) 0,rgba(150,120,90,0) 300px),
  linear-gradient(180deg,#fdf6e6 0%,#f3ddb0 55%,#e3c99a 100%)}
.blog-title{position:absolute;top:55px;width:100%;text-align:center;font-family:"Dancing Script",cursive;font-size:34px;color:var(--gold)}
.post-img{position:absolute;width:210px;height:166px}
.post-date{position:absolute;width:100%;text-align:center;font-family:"Jost",sans-serif;color:#fff}
.post-box{position:absolute;background:#fff;width:326px;height:166px;text-align:center;color:var(--blog-text);font-family:"Jost",sans-serif}
.post-h{font-family:"Jost",sans-serif;font-weight:500;font-size:20px;color:var(--gold)}
.post-meta{font-size:12px;color:#555;margin-top:10px;display:flex;justify-content:center;gap:10px;align-items:center}
.post-meta svg{vertical-align:middle;margin-right:4px}
.post-more{display:inline-block;margin-top:18px;font-size:13px;font-weight:500;color:#222;border-bottom:1px solid #222;padding-bottom:2px}

/* footer */
.footer{top:2875px;height:212px;background:var(--footer)}
.footer-bar{top:3087px;height:65px;background:var(--footer-bar);display:flex;align-items:center;justify-content:center;font-size:12px;color:#bbb}
.foot-small{font-family:"Jost",sans-serif;font-size:12px;line-height:21px;color:#ddd;white-space:nowrap}
.social{position:absolute;top:2951px;width:30px;height:30px;border-radius:50%;background:#55555a}
</style>
</head>
<body>

<!-- hero -->
<section class="section hero">
  <div class="hero-photo" role="img" aria-label="Top-down photo of Korean dishes and grilled meat on a wooden table"></div>
  <div class="hero-shade"></div>
  <div class="brand">EMBERLY</div>
  <nav class="nav">
    <a style="left:603px">Home</a>
    <a style="left:672px">Menu</a>
    <a style="left:759px">About us</a>
    <a style="left:830px">Book</a>
    <a style="left:897px">Events</a>
    <a style="left:975px">Blog</a>
    <a style="left:1036px">Contact</a>
  </nav>
  <h1 class="hero-title">HEALTHY &amp; TASTY</h1>
  <p class="hero-sub">Enjoy the real fresh food from our chef.</p>
  <div class="btn btn-outline" style="left:487px;top:410px;width:110px;height:36px">Book now</div>
  <div class="btn btn-gold" style="left:607px;top:410px;width:110px;height:36px">View menu</div>
</section>

<!-- book + welcome -->
<section class="section book">
  <div class="wood" role="img" aria-label="Dark wooden plank background"></div>
  <div class="wood-shade"></div>
  <div class="book-panel">
    <h2 class="sec-title abs" style="top:60px;width:468px;text-align:center">Book a table</h2>
    <div class="rule abs" style="left:210px;top:106px"></div>
  </div>
  <div class="field" style="left:170px;top:154px;width:105px;height:31px">Date</div>
  <div class="field" style="left:300px;top:154px;width:105px;height:31px">Time</div>
  <div class="field" style="left:430px;top:154px;width:108px;height:31px">Person</div>
  <div class="field" style="left:170px;top:213px;width:170px;height:31px">Your Name</div>
  <div class="field" style="left:365px;top:213px;width:173px;height:31px">Your Email</div>
  <div class="field" style="left:170px;top:271px;width:368px;height:139px">Any Message?</div>
  <div class="btn btn-gold" style="left:290px;top:435px;width:126px;height:36px">Submit form</div>

  <h2 class="sec-title abs" style="left:697px;top:76px">Welcome to Emberly</h2>
  <div class="script abs" style="left:697px;top:112px">The Art of Cookings</div>
  <div class="rule abs" style="left:697px;top:163px;width:40px"></div>
</section>
<p class="welcome-text">Lorem ipsum dolor sit amet, consectetur adipiscing elit, sed do eiusmod tempor incididunt ut labore et dolore magna aliqua. Ut enim ad minim veniam, quis nostrud exercitation ullamco laboris nisi ut aliquip ex ea commodo consequat. Duis aute irure dolor in reprehenderit in voluptate velit esse cillum dolore eu fugiat nulla pariatur. Excepteur sint occaecat cupidatat non proident, sunt in culpa qui officia deserunt mollit anim id est laborum.</p>

<!-- today's special -->
<section class="section special">
  <div class="special-bg" role="img" aria-label="Dark kitchen table with a wooden board, bread, garlic and a mortar"></div>
  <h2 class="sec-title abs" style="top:65px;width:100%;text-align:center">Today's Special</h2>
  <div class="script abs" style="top:100px;width:100%;text-align:center;font-size:17px">Fresh and delicious</div>
  <div class="rule abs" style="left:576px;top:155px"></div>
</section>
<div class="dish" style="left:120px">
  <div class="dish-photo" role="img" aria-label="Roasted chicken" style="background:radial-gradient(circle at 45% 50%,#e0a050 0,#b8602a 45%,#2a1a12 100%)"></div>
  <div class="dish-name">Roasted Chicken</div><div class="dish-rule"></div><div class="dish-price">$55</div>
</div>
<div class="dish" style="left:365px">
  <div class="dish-photo" role="img" aria-label="Baked crab cheese balls with dip" style="background:radial-gradient(circle at 50% 65%,#d9a066 0,#e8dcc8 40%,#5c93b8 100%)"></div>
  <div class="dish-name">Baked Crab Cheese</div><div class="dish-rule"></div><div class="dish-price">$66</div>
</div>
<div class="dish" style="left:611px">
  <div class="dish-photo" role="img" aria-label="Sliced foie gras with spices" style="background:radial-gradient(circle at 55% 45%,#f6e8da 0,#e2c4a8 45%,#8a6a48 100%)"></div>
  <div class="dish-name">Foie Gras</div><div class="dish-rule"></div><div class="dish-price">$99</div>
</div>
<div class="dish" style="left:857px">
  <div class="dish-photo" role="img" aria-label="Chicken satay skewers with onion" style="background:radial-gradient(circle at 50% 55%,#6a2418 0,#9a3a2a 40%,#4a7a30 100%)"></div>
  <div class="dish-name">Chicken Satay</div><div class="dish-rule"></div><div class="dish-price">$56</div>
</div>

<!-- menu -->
<section class="section menu">
  <h2 class="sec-title abs" style="top:40px;width:100%;text-align:center">Our Menu</h2>
  <div class="script abs" style="top:78px;width:100%;text-align:center;font-size:17px">Healthy &amp; Tasty</div>
  <div class="rule abs" style="left:576px;top:130px"></div>
  <div class="tab active" style="left:441px">MAINS</div>
  <div class="tab" style="left:545px">STARTER</div>
  <div class="tab" style="left:662px">DRINKS</div>

  <div class="item" style="left:183px;top:248px"><div class="item-thumb" role="img" aria-label="Chicken crispy roll" style="background:radial-gradient(circle,#e8c060,#8a6a20)"></div><div class="item-name">Chicken Crispy Roll</div><div class="item-price">$66</div><div class="item-desc">Lorem ipsum dolor sit amet, consectetur adipiscing elit, sed do eiusmod tempor incididunt ut labore et dolore magna aliqua.</div></div>
  <div class="item" style="left:613px;top:248px"><div class="item-thumb" role="img" aria-label="Cheese shrimp roll" style="background:radial-gradient(circle,#d8d8d8,#4a4a4a)"></div><div class="item-name">Cheese Shrimp Roll</div><div class="item-price">$42</div><div class="item-desc">Lorem ipsum dolor sit amet, consectetur adipiscing elit, sed do eiusmod tempor incididunt ut labore et dolore magna aliqua.</div></div>
  <div class="item" style="left:183px;top:340px"><div class="item-thumb" role="img" aria-label="Baked crab cheese" style="background:radial-gradient(circle,#e0b07a,#6a9ab8)"></div><div class="item-name">Baked Crab Cheese</div><div class="item-price">$66</div><div class="item-desc">Lorem ipsum dolor sit amet, consectetur adipiscing elit, sed do eiusmod tempor incididunt ut labore et dolore magna aliqua.</div></div>
  <div class="item" style="left:613px;top:340px"><div class="item-thumb" role="img" aria-label="Crispy squid" style="background:radial-gradient(circle,#f0c840,#9a7010)"></div><div class="item-name">Crispy Squid</div><div class="item-price">$54</div><div class="item-desc">Lorem ipsum dolor sit amet, consectetur adipiscing elit, sed do eiusmod tempor incididunt ut labore et dolore magna aliqua.</div></div>
  <div class="item" style="left:183px;top:434px"><div class="item-thumb" role="img" aria-label="Foie gras" style="background:radial-gradient(circle,#f4e6d6,#b8987a)"></div><div class="item-name">Foie Gras</div><div class="item-price">$99</div><div class="item-desc">Lorem ipsum dolor sit amet, consectetur adipiscing elit, sed do eiusmod tempor incididunt ut labore et dolore magna aliqua.</div></div>
  <div class="item" style="left:613px;top:434px"><div class="item-thumb" role="img" aria-label="Roasted chicken" style="background:radial-gradient(circle,#e07a3a,#7a2a10)"></div><div class="item-name">Roasted Chicken</div><div class="item-price">$55</div><div class="item-desc">Lorem ipsum dolor sit amet, consectetur adipiscing elit, sed do eiusmod tempor incididunt ut labore et dolore magna aliqua.</div></div>
</section>

<!-- blog -->
<section class="section blog">
  <div class="blog-bg" role="img" aria-label="Blurred sunlit restaurant terrace"></div>
  <h2 class="blog-title">Our Blog</h2>
  <div class="abs" role="img" aria-label="Decorative divider under the blog heading" style="left:430px;top:112px;width:340px;height:6px;background:linear-gradient(90deg,rgba(200,150,62,0),rgba(200,150,62,.75) 30%,rgba(200,150,62,.75) 70%,rgba(200,150,62,0))"></div>

  <div class="post-img" role="img" aria-label="Plated fresh food with herbs" style="left:124px;top:176px;background:radial-gradient(circle at 35% 40%,#8a6a3a 0,#4a3a2a 45%,#1e1a16 100%)">
    <div class="post-date" style="top:44px;font-size:42px;line-height:44px">12</div>
    <div class="post-date" style="top:92px;font-size:10px">JUNE</div>
  </div>
  <div class="post-box" style="left:334px;top:176px;padding-top:38px">
    <div class="post-h">Kinds of fresh food</div>
    <div class="post-meta"><span>RESTAURANT</span><span><svg width="12" height="12" viewBox="0 0 12 12"><circle cx="6" cy="6" r="5" fill="none" stroke="#555"/><path d="M6 3 V6 H8.5" fill="none" stroke="#555"/></svg>8:42 am - 7:51 am</span></div>
    <span class="post-more">View More</span>
  </div>
  <div class="post-img" role="img" aria-label="Steak served on a slate table setting" style="left:124px;top:357px;background:radial-gradient(circle at 40% 55%,#9a5a3a 0,#5a4a40 45%,#2a2420 100%)">
    <div class="post-date" style="top:44px;font-size:42px;line-height:44px">12</div>
    <div class="post-date" style="top:92px;font-size:10px">SEPTEMBER</div>
  </div>
  <div class="post-box" style="left:334px;top:357px;padding-top:38px">
    <div class="post-h">Table decoration trends</div>
    <div class="post-meta"><span>RECIPE</span><span><svg width="12" height="12" viewBox="0 0 12 12"><circle cx="6" cy="6" r="5" fill="none" stroke="#555"/><path d="M6 3 V6 H8.5" fill="none" stroke="#555"/></svg>7:10 pm - 7:51 am</span></div>
    <span class="post-more">View More</span>
  </div>

  <div class="abs" role="img" aria-label="Diners raising glasses at a restaurant table" style="left:678px;top:176px;width:400px;height:346px;background:radial-gradient(ellipse at 20% 30%,#3a2a1e 0,#6a503a 40%,#d8bf98 80%,#a88a66 100%)"></div>
  <div class="abs" style="left:703px;top:205px;width:347px;height:284px;background:#fff;text-align:center;font-family:'Jost',sans-serif;color:#333">
    <div class="post-h" style="margin-top:116px">Top 99 Restaurants</div>
    <div class="post-meta"><span>DRINKS</span><span><svg width="12" height="12" viewBox="0 0 12 12"><circle cx="6" cy="6" r="5" fill="none" stroke="#555"/><path d="M6 3 V6 H8.5" fill="none" stroke="#555"/></svg>8:32 am - 7:47 am</span></div>
    <span class="post-more">View More</span>
  </div>
  <svg class="abs" style="left:856px;top:488px" width="44" height="20"><path d="M0 0 H44 L22 20 Z" fill="#fff"/></svg>
  <div class="abs" style="left:836px;top:176px;width:84px;height:91px;background:var(--gold);text-align:center;font-family:'Jost',sans-serif">
    <div style="font-size:38px;line-height:44px;margin-top:16px">06</div>
    <div style="font-size:10px">MAY</div>
  </div>
</section>

<!-- footer -->
<footer class="section footer">
  <div class="abs" style="left:26px;top:36px;font-family:'Oswald',sans-serif;font-weight:600;font-size:34px;letter-spacing:3px">EMBERLY</div>
  <div class="foot-small abs" style="left:30px;top:114px;font-size:10px">RECOMENDED BY</div>
  <div class="abs" style="left:30px;top:140px;width:150px;height:30px;border-radius:15px;background:#3a3a3e"></div>
  <div class="foot-small abs" style="left:225px;top:46px">48 Cedar Row, Ashford Lane, Millbrook<br>RESERVATIONS NUMBER:  +00 41 302 66190</div>
  <div class="foot-small abs" style="left:225px;top:100px">WORKING HOURS:<br>MON - FRI: 08:00 AM - 10:00 PM<br>SAT - SUN: 10:00 AM - 11:00 PM</div>
  <div class="abs" style="left:689px;top:42px;font-family:'Jost',sans-serif;font-size:14px">FOLLOW US AT</div>
  <div class="abs" style="left:808px;top:42px;font-family:'Jost',sans-serif;font-size:14px">NEWSLETTER</div>
  <div class="abs" style="left:808px;top:78px;width:236px;height:34px;background:#fff;color:#888;font-size:11px;padding:10px 14px">Email Address</div>
  <div class="abs" style="left:1044px;top:78px;width:103px;height:34px;background:#f0bb1e;color:#fff;font-size:12px;display:flex;align-items:center;justify-content:center">Sign Up Now</div>
</footer>
<div class="social" style="left:636px"></div>
<div class="social" style="left:673px"></div>
<div class="social" style="left:710px"></div>
<div class="social" style="left:747px"></div>
<div class="abs" style="left:1160px;top:3040px;width:26px;height:30px;background:#c9762a;border-radius:2px;display:flex;align-items:center;justify-content:center">
  <svg width="10" height="12" viewBox="0 0 10 12"><path d="M5 1 V11 M1 5 L5 1 L9 5" fill="none" stroke="#1a1a1a" stroke-width="2"/></svg>
</div>
<div class="section footer-bar">Copyright © 2017 Emberly Smokehouse. All Rights Reserved.</div>

</body>
</html>
```